Health Supplement Series for 60 tablets of pure Gold Petal Grain powder

We need a packaging design theme for a health supplement for international consumers. Our initial product is called 'Gold Petal Grain'. It is for general health and is particularly effective for diabetic symptoms.
We would like to see designs that are clean and fresh.
It should give the impression of professional, premium pharmaceutical grade products.
Our company logo is attached below.

Target Market(s)

International

Industry/Entity Type

Health And Wellness

Font styles to use
Serif
Sans Serif

Requirements
Must have
• Bottle and box packaging required.
• 1st product is bottle of 60 tablets of 0.5gm each.
Should not have
• Seals and other "must buy" "guaranteed" etc

```html
<!DOCTYPE html>
<html lang="en">
<head>
<meta charset="utf-8">
<title>Gold Petal Grain – Packaging</title>
<link rel="stylesheet" href="https://fonts.googleapis.com/css2?family=Roboto+Condensed:wght@400;700&display=swap">
<style>
  :root {
    --green: #5cae1c;
    --green-dark: #2e7a12;
    --white: #ffffff;
    --paper: #fbfcfb;
    --backdrop: #e6edf4;
    --ink-green: #4f9d18;
  }
  * { margin: 0; padding: 0; box-sizing: border-box; }
  html, body { width: 1200px; height: 886px; overflow: hidden; }
  body {
    background: var(--backdrop);
    font-family: "Roboto Condensed", "Arial Narrow", sans-serif;
    position: relative;
  }

  /* ---------- shared brand lockup ---------- */
  .brand { display: flex; align-items: center; gap: 8px; color: var(--green); }
  .brand-square { width: 30px; height: 30px; background: var(--green); flex: none; }
  .brand-text { font-weight: 700; line-height: 1; }
  .brand-name { display: block; font-size: 34px; letter-spacing: 3px; }
  .brand-sub { display: block; font-size: 13px; letter-spacing: 0.5px; margin-top: 2px; }

  /* ---------- name band ---------- */
  .name-band { position: absolute; left: 0; width: 100%; }
  .name-band svg { position: absolute; inset: 0; width: 100%; height: 100%; }
  .name-top, .name-bottom { position: absolute; font-weight: 700; line-height: 1; }
  .name-top { color: var(--white); }
  .name-bottom { color: var(--green); }

  /* ---------- bottle label (flat wrap) ---------- */
  .bottle-label {
    position: absolute; left: 70px; top: 190px;
    width: 540px; height: 430px;
    background: var(--paper);
    box-shadow: 0 1px 0 rgba(0,0,0,0.05);
  }
  .bottle-label .edge-stripe {
    position: absolute; left: 0; top: 0; bottom: 0; width: 16px; background: var(--green);
  }
  .bottle-label .top-rule {
    position: absolute; left: 16px; right: 0; top: 14px; height: 4px; background: var(--green);
  }
  .bottle-label .bottom-bar {
    position: absolute; left: 16px; right: 0; bottom: 0; height: 16px; background: var(--green);
  }
  .bottle-label .brand { position: absolute; left: 150px; top: 70px; }
  .bottle-label .name-band { top: 190px; height: 110px; }
  .bottle-label .name-top { left: 180px; top: 12px; font-size: 36px; }
  .bottle-label .name-bottom { left: 300px; top: 52px; font-size: 50px; }
  .bottle-label .supplement {
    position: absolute; left: 0; right: 0; top: 340px; text-align: center;
    color: var(--ink-green); font-size: 16px; font-weight: 400;
  }
  .bottle-label .dose-row {
    position: absolute; left: 0; right: 0; top: 370px;
    display: flex; justify-content: center; gap: 40px;
    color: var(--ink-green); font-size: 22px; font-weight: 700;
  }

  /* ---------- box (flat side + front) ---------- */
  .box { position: absolute; left: 690px; top: 130px; height: 626px; display: flex; }
  .box-side {
    position: relative; width: 140px; height: 100%;
    background: var(--paper); border-right: 1px solid #dfe5dc;
  }
  .box-side .side-top { position: absolute; left: 0; right: 0; top: 0; height: 28px; background: var(--green-dark); }
  .box-side .side-band { position: absolute; left: 0; right: 0; top: 300px; height: 170px; background: var(--green-dark); }
  .box-side .side-bottom { position: absolute; left: 0; right: 0; bottom: 0; height: 50px; background: var(--green-dark); }
  .side-copy {
    position: absolute; left: 12px; right: 12px;
    font-size: 9px; line-height: 1.35; color: #333;
  }
  .side-copy.usage { top: 90px; }
  .side-copy.directions { top: 318px; color: var(--white); }

  .box-front { position: relative; width: 320px; height: 100%; background: var(--white); }
  .box-front .front-top { position: absolute; left: 0; right: 0; top: 0; height: 28px; background: var(--green); }
  .box-front .brand { position: absolute; left: 78px; top: 96px; }
  .box-front .brand-name { font-size: 30px; }
  .box-front .brand-sub { font-size: 12px; }
  .box-front .name-band { top: 290px; height: 160px; }
  .box-front .name-top { left: 60px; top: 24px; font-size: 38px; color: var(--green); }
  .box-front .name-bottom { left: 110px; top: 72px; font-size: 50px; color: var(--white); }
  .box-front .supplement {
    position: absolute; left: 0; right: 0; top: 536px; text-align: center;
    color: var(--ink-green); font-size: 17px;
  }
  .box-front .count-bar {
    position: absolute; left: 0; right: 0; bottom: 0; height: 50px; background: var(--green);
    display: flex; align-items: center; justify-content: flex-end; padding-right: 40px;
    color: var(--white); font-size: 22px; font-weight: 700;
  }
</style>
</head>
<body>

  <!-- Bottle label -->
  <section class="bottle-label" aria-label="Bottle label">
    <div class="edge-stripe"></div>
    <div class="top-rule"></div>

    <div class="brand">
      <span class="brand-square"></span>
      <span class="brand-text">
        <span class="brand-name">NORVANE</span>
        <span class="brand-sub">BIOTECH LIMITED</span>
      </span>
    </div>

    <div class="name-band">
      <svg viewBox="0 0 540 110" preserveAspectRatio="none" aria-hidden="true">
        <rect x="16" y="0" width="454" height="4" fill="var(--green)"/>
        <polygon points="16,8 470,8 430,100 16,100" fill="var(--green)"/>
        <polygon points="290,50 440,50 420,98 270,98" fill="var(--white)"/>
        <rect x="16" y="104" width="410" height="3" fill="var(--green)"/>
      </svg>
      <span class="name-top">Gold Petal</span>
      <span class="name-bottom">Grain</span>
    </div>

    <p class="supplement">DIETARY SUPPLEMENT</p>
    <div class="dose-row"><span>500mg</span><span>60 Tablets</span></div>

    <div class="bottom-bar"></div>
  </section>

  <!-- Box -->
  <section class="box" aria-label="Carton">
    <div class="box-side">
      <div class="side-top"></div>
      <p class="side-copy usage">Made from finely milled grain and petal extract, each tablet is pressed to a steady dose for daily use. Store in a cool dry place away from light. Keep the lid closed after each use. Not intended to diagnose or treat any disease.</p>
      <div class="side-band"></div>
      <p class="side-copy directions">Directions: take one tablet twice a day with water, or as advised by your doctor. Do not exceed the stated dose. Keep out of reach of children.</p>
      <div class="side-bottom"></div>
    </div>

    <div class="box-front">
      <div class="front-top"></div>

      <div class="brand">
        <span class="brand-square"></span>
        <span class="brand-text">
          <span class="brand-name">NORVANE</span>
          <span class="brand-sub">BIOTECH LIMITED</span>
        </span>
      </div>

      <div class="name-band">
        <svg viewBox="0 0 320 160" preserveAspectRatio="none" aria-hidden="true">
          <path d="M0,10 H320 V150 H0 Z" fill="var(--green)"/>
          <path d="M40,18 H300 L250,140 H40 Q34,140 34,132 V24 Q34,18 40,18 Z" fill="var(--white)"/>
          <polygon points="120,70 270,70 246,132 96,132" fill="var(--green)"/>
        </svg>
        <span class="name-top">Gold Petal</span>
        <span class="name-bottom">Grain</span>
      </div>

      <p class="supplement">DIETARY SUPPLEMENT</p>
      <div class="count-bar">60 Tablets</div>
    </div>
  </section>

</body>
</html>
```